Corporate Intelligence Agency seeks redesign *

Brightfen Advisory is a business intelligence firm made up of former special operations and intelligence professionals. Our vibe is quiet professionals that get the job done by whatever means necessary.
Our aesthetic is clean, sleek, and monochromatic. We prefer the texture contrasts over colors. Slick white or black, playing up textures, and bold block lettering, and simplicity are what we are looking for in a design.

The logo would preferably pay homage to our military/special operations roots, and the culture of changing for the better (alchemy) that we embody all while remaining simple.

Target Market(s)

C-Level executives with a taste for the simple over the extravagant, and cut right to the chase

Industry/Entity Type

Management Solution

Contact Information for Business Card

Back is matte black with a glossy black logo to contrast. The front has the logo, with space on the bottom left for name and contact

Logo Text

Brightfen Adv.

Logo styles of interest
Abstract Logo
Wordmark Logo
Lettermark Logo
Font styles to use
Serif
Sans Serif
Script

Requirements
Must have
• Monochromatic, play on texture within card (the card ought to be memorable to hold), solid/clean lettering. Logo should be simple and sleek.
Nice to have
• If the logo can tie alchemy and intelligence/spy genre. 3d textures
Should not have
• Nothing overtly military. No colors outside of the monochromatic spectrum

```html
<!DOCTYPE html>
<html lang="en">
<head>
<meta charset="utf-8">
<title>Brightfen Advisory — Business Card</title>
<link rel="stylesheet" href="https://fonts.googleapis.com/css2?family=Josefin+Sans:wght@300;400;600&display=swap">
<style>
  :root {
    --backdrop: #f1f1f2;
    --card: #333333;
    --ink: #ffffff;
    --ink-soft: #d9d9d9;
  }
  * { margin: 0; padding: 0; box-sizing: border-box; }
  html, body {
    width: 1200px;
    height: 1200px;
    overflow: hidden;
    background: var(--backdrop);
  }
  .canvas {
    width: 1200px;
    height: 1200px;
    display: flex;
    align-items: center;
    justify-content: center;
  }
  .business-card {
    position: relative;
    width: 840px;
    height: 504px;
    background: var(--card);
    font-family: "Josefin Sans", sans-serif;
    color: var(--ink);
  }
  .brand {
    position: absolute;
    left: 158px;
    top: 150px;
    display: flex;
    align-items: flex-start;
    gap: 22px;
    font-weight: 400;
    color: var(--ink);
  }
  .brand-mark {
    width: 22px;
    height: 22px;
    background: var(--ink);
    margin-top: 16px;
  }
  .brand-name {
    display: flex;
    flex-direction: column;
  }
  .brand-primary {
    font-size: 74px;
    line-height: 1;
    letter-spacing: 6px;
  }
  .brand-secondary {
    font-size: 27px;
    line-height: 1;
    letter-spacing: 15px;
    margin-top: 10px;
  }
  .contact {
    position: absolute;
    left: 158px;
    top: 318px;
  }
  .contact-item + .contact-item { margin-top: 22px; }
  .contact-label {
    font-weight: 600;
    font-size: 16px;
    letter-spacing: 1.5px;
    text-transform: uppercase;
    color: var(--ink);
  }
  .contact-value {
    font-weight: 300;
    font-size: 18px;
    letter-spacing: 0.8px;
    margin-top: 6px;
    color: var(--ink-soft);
  }
</style>
</head>
<body>
  <main class="canvas">
    <article class="business-card">
      <div class="brand">
        <span class="brand-mark" aria-hidden="true"></span>
        <div class="brand-name">
          <span class="brand-primary">BRIGHTFEN</span>
          <span class="brand-secondary">ADVISORY</span>
        </div>
      </div>
      <div class="contact">
        <div class="contact-item">
          <p class="contact-label">Phone</p>
          <p class="contact-value">555 014 2290</p>
        </div>
        <div class="contact-item">
          <p class="contact-label">Website</p>
          <p class="contact-value">brightfenadvisory.com</p>
        </div>
      </div>
    </article>
  </main>
</body>
</html>
```